"Word Cloud" lists of countries, by decade, who have adopted women's suffrage

The winning designer will (eventually, but not necessarily within this project--see "Nice to Haves", below) design a total of eight images, based on the eight lists of countries (see attached files) in order, by decade, that they adopted women's suffrage.

One of the the attached images is a screen shot of five pages of the book KITE: Notes Toward a Borderless Tomorrow, showing how these lists are presently arranged on 6"x9" pages.

We essentially want to spice up these 8 lists and make them more fun to look at, for the reader.

Target Market(s)

General audience. People who want to make a difference. People who want to do something to change the world, and want to read a book about how we can actually do it.

Industry/Entity Type

Political

Font styles to use
Serif
Sans Serif
Decorative
Script

Requirements
Must have
• At least two initial designs, one for each of the two largest lists (lists 5 and 6). All country names must be spelled correctly. A WORD doc has been provided with all the text you need to work with. An EXAMPLE word cloud has been provided for inspiration. The look and feel of these "Country Clouds" wants to go all over the place, but all names should be (at least somewhat) readable.
• IMPORTANT ELEMENTS: (1) There are a few places where current countries were just one, when they got women's suffrage. Keep this info intact, together, in the cloud. EXAMPLE (from list 6):
•  British Leeward Islands (remove ", including today’s:", but keep together with)
•  Antigua and Barbuda
•  British Virgin Islands
•  Montserrat
•  Saint Kitts and Nevis
•  Anguilla
• (2) The names of the countries should stay in roughly the same order as found in the lists, but laid out (very) roughly right to left and then top to bottom, loosely akin to the standard flow of text written in the latin alphabet. It is fine to alter this standard in minor ways to achieve a better look to the design. Just don't move a country found at the top of one list into the middle of that list or down to the bottom, etc.
• These country clouds will be printed in black and white, so keep the designs greyscale.
• These "country clouds" should be 4.5" in width.The largest country clouds, with the most countries found in them, should not exceed 6" in length.
Nice to have
• (Eventually) all 8 lists in the form of "Country Clouds"---that are playful, but with serious elements. Pull up a list of countries by population, have the 20 biggest use the biggest font sizes. Use many different fonts, mix it up! Essentially, these 8 lists all want to become word clouds, with each nation's full name as its own "word." See example cloud.
• Though having all 8 lists in clouds at the end of this project is "nice to have," the winner for this design might simply produce 2 such clouds, along with a cost estimate attached to the submitted design for what they would charge to complete the other 6 clouds.
Should not have
• Do NOT include the textual transitions found between the lists, in the screen shot or word doc. They are there just to help you see how the different graphics will be used and what will go either before or after them.
• No need to use bullet points.

```html
<!DOCTYPE html>
<html lang="en">
<head>
<meta charset="utf-8">
<title>Country Cloud – Women's Suffrage by Decade</title>
<link rel="stylesheet" href="https://fonts.googleapis.com/css2?family=Alfa+Slab+One&family=Aladin&family=Anton&family=Arvo:ital,wght@1,700&family=Bungee&family=Cinzel:wght@500&family=Comfortaa:wght@700&family=Cormorant+SC:wght@600&family=Fredoka:wght@500;600&family=Kaushan+Script&family=Lato:wght@400&family=Lilita+One&family=Lobster&family=Montserrat:wght@700;800;900&family=Open+Sans:ital,wght@0,400;0,800;1,400&family=Oswald:wght@700&family=PT+Serif&family=Passion+One&family=Poiret+One&family=Quicksand:wght@400&family=Righteous&family=Roboto+Condensed:wght@700&family=Varela+Round&display=swap">
<style>
  :root {
    --paper: #ffffff;
    --ink: #333333;
    --ink-mid: #4a4a4a;
    --ink-soft: #5c5c5c;
    --rule: #d6d6d6;
  }
  html, body {
    margin: 0;
    padding: 0;
    width: 800px;
    height: 1200px;
    overflow: hidden;
    background: var(--paper);
  }
  .country-cloud {
    position: relative;
    width: 800px;
    height: 1200px;
    color: var(--ink);
  }
  .country {
    position: absolute;
    margin: 0;
    line-height: 1;
    white-space: nowrap;
  }
  .vertical-down { writing-mode: vertical-rl; }
  .vertical-up { writing-mode: vertical-rl; transform: rotate(180deg); }

  .former-union {
    position: absolute;
    left: 154px; top: 373px;
    width: 147px; height: 189px;
    border: 1px solid var(--rule);
    border-radius: 6px;
  }

  .panama { left: 120px; top: 270px; font: 800 34px "Montserrat", sans-serif; letter-spacing: 5px; color: var(--ink-mid); }
  .dominican-republic { left: 332px; top: 272px; font: 500 29px "Fredoka", sans-serif; letter-spacing: 1px; }
  .france { left: 120px; top: 300px; font: 68px "Anton", sans-serif; letter-spacing: 1px; }
  .jamaica { left: 334px; top: 300px; font: 44px "Lilita One", sans-serif; letter-spacing: 1px; }
  .senegal { left: 528px; top: 303px; font: 31px "Varela Round", sans-serif; color: var(--ink-soft); }
  .guatemala { left: 334px; top: 341px; font: 26px "Bungee", sans-serif; letter-spacing: 2px; color: var(--ink-mid); }
  .togo { left: 570px; top: 340px; font: 26px "Righteous", sans-serif; letter-spacing: 2px; }
  .bermuda { left: 668px; top: 270px; font: 900 17px "Montserrat", sans-serif; letter-spacing: 1px; }

  .yugoslavia { left: 120px; top: 382px; font: 900 27px "Montserrat", sans-serif; }
  .serbia { left: 174px; top: 380px; font: italic 400 26px "Open Sans", sans-serif; }
  .montenegro { left: 170px; top: 412px; font: 24px "Poiret One", sans-serif; }
  .croatia { left: 174px; top: 442px; font: 800 20px "Montserrat", sans-serif; letter-spacing: 1px; }
  .bosna { left: 177px; top: 469px; font: 400 16px "Lato", sans-serif; }
  .herzegovina { left: 177px; top: 490px; font: 400 16px "Lato", sans-serif; }
  .macedonia { left: 174px; top: 512px; font: 19px "Aladin", cursive; }
  .slovenia { left: 174px; top: 537px; font: 800 18px "Montserrat", sans-serif; letter-spacing: 1px; }

  .cameroon { left: 314px; top: 392px; font: italic 700 29px "Arvo", serif; }
  .djibouti { left: 318px; top: 432px; font: 44px "Passion One", sans-serif; }
  .liberia { left: 320px; top: 491px; font: 700 24px "Montserrat", sans-serif; letter-spacing: 2px; color: var(--ink-mid); }
  .venezuela { left: 316px; top: 531px; font: 400 22px "Open Sans", sans-serif; letter-spacing: 2px; color: var(--ink-soft); }
  .vietnam { left: 486px; top: 386px; font: 800 29px "Montserrat", sans-serif; letter-spacing: 2px; }
  .north { left: 534px; top: 384px; font: 700 54px "Oswald", sans-serif; }
  .korea { left: 534px; top: 446px; font: 700 54px "Oswald", sans-serif; }
  .argentina { left: 532px; top: 508px; font: 800 29px "Open Sans", sans-serif; color: var(--ink-mid); }

  .china { left: 120px; top: 570px; font: 58px "PT Serif", serif; }
  .including { left: 313px; top: 579px; font: 14px "PT Serif", serif; letter-spacing: 2px; }
  .taiwan { left: 313px; top: 592px; font: 700 31px "Roboto Condensed", sans-serif; }
  .india { left: 452px; top: 562px; font: 64px "Alfa Slab One", serif; letter-spacing: 2px; }

  .malta { left: 318px; top: 634px; font: italic 700 30px "Arvo", serif; }
  .pakistan { left: 444px; top: 636px; font: 400 32px "Quicksand", sans-serif; letter-spacing: 10px; }
  .japan { left: 120px; top: 642px; font: 56px "Lilita One", sans-serif; letter-spacing: 1px; }
  .singapore { left: 302px; top: 676px; font: 800 23px "Montserrat", sans-serif; letter-spacing: 1px; color: var(--ink-mid); }
  .israel { left: 478px; top: 664px; font: 600 44px "Cormorant SC", serif; letter-spacing: 4px; }
  .chile { left: 646px; top: 672px; font: 700 42px "Comfortaa", sans-serif; }

  .south-korea { left: 118px; top: 700px; font: 46px "Kaushan Script", cursive; }
  .niger { left: 386px; top: 714px; font: 40px "Passion One", sans-serif; letter-spacing: 1px; }
  .seychelles { left: 512px; top: 710px; font: italic 700 25px "Arvo", serif; }
  .suriname { left: 532px; top: 749px; font: 400 17px "Lato", sans-serif; letter-spacing: 2px; color: var(--ink-soft); }
  .costa-rica { left: 116px; top: 758px; font: 36px "Lobster", cursive; }
  .hong-kong { left: 274px; top: 762px; font: 800 22px "Montserrat", sans-serif; }
  .hong-kong-note { left: 270px; top: 786px; font: 700 12px "Montserrat", sans-serif; }
  .antilles { left: 430px; top: 768px; font: 27px "Anton", sans-serif; }
  .syria { left: 536px; top: 768px; font: 500 25px "Cinzel", serif; letter-spacing: 1px; }
</style>
</head>
<body>
<main class="country-cloud" aria-label="Countries adopting women's suffrage in this decade">
  <p class="country panama">PANAMA</p>
  <p class="country dominican-republic">DOMINICAN REPUBLIC</p>
  <p class="country france">FRANCE</p>
  <p class="country jamaica">Jamaica</p>
  <p class="country senegal">Senegal</p>
  <p class="country guatemala">GUATEMALA</p>
  <p class="country togo">TOGO</p>
  <p class="country bermuda vertical-down">BERMUDA</p>

  <p class="country yugoslavia vertical-up">YUGOSLAVIA</p>
  <div class="former-union"></div>
  <p class="country serbia">Serbia</p>
  <p class="country montenegro">Montenegro</p>
  <p class="country croatia">CROATIA</p>
  <p class="country bosna">Bosna and</p>
  <p class="country herzegovina">Herzegovina</p>
  <p class="country macedonia">MACEDONIA</p>
  <p class="country slovenia">SLOVENIA</p>

  <p class="country cameroon">Cameroon</p>
  <p class="country djibouti">DJIBOUTI</p>
  <p class="country liberia">LIBERIA</p>
  <p class="country venezuela">VENEZUELA</p>
  <p class="country vietnam vertical-up">VIETNAM</p>
  <p class="country north">NORTH</p>
  <p class="country korea">KOREA</p>
  <p class="country argentina">Argentina</p>

  <p class="country china">CHINA</p>
  <p class="country including">INCLUDING</p>
  <p class="country taiwan">TAIWAN</p>
  <p class="country india">INDIA</p>

  <p class="country malta">Malta</p>
  <p class="country pakistan">pakistan</p>
  <p class="country japan">japan</p>
  <p class="country singapore">SINGAPORE</p>
  <p class="country israel">Israel</p>
  <p class="country chile vertical-up">CHILE</p>

  <p class="country south-korea">South Korea</p>
  <p class="country niger">NIGER</p>
  <p class="country seychelles">Seychelles</p>
  <p class="country suriname">SURINAME</p>
  <p class="country costa-rica">Costa Rica</p>
  <p class="country hong-kong">HONG KONG</p>
  <p class="country hong-kong-note">(NOW PART OF CHINA)</p>
  <p class="country antilles">ANTILLES</p>
  <p class="country syria">Syria</p>
</main>
</body>
</html>
```